"Principles for action" poster design for inside company

I would like to create a poster in order to make a message from CEO to employees to be clearly.
A size is A3E(landscape) , and I wish you to design 3 messages(principles for action) into one poster.
("Principles for action" is core value for employees to do everything on working in our company.)
I want you to design and place 3 messages as if they have some relations each other in one poster.
Principles for actions are as follows;
(1)Bird's eye view:
(Meaning: Although there are multiple right answers, it is difficult to gain something if you do not have different view from common one. We request you always to compare subjective view and objective view and then aim to have the specific view.)
(2)Agility:
(Meaning: Maximum rapidity is obtained in any case. Rapid accumulation of trivial reply, delivery, and courtesy, and it will lead to overall competitiveness.)
(3)Back to comfort:
(Meaning:Whatever the type of business be, various ideas are generated by employees. Those born in uncomfortable environment, become bad product that are not comfortable. In other words, managers will be asked to keep the comfortable environment.)
(Summary)
Our company always require employees that "First, you grasp the meaning of everything as if having bird's eyes, and do action rapidly. if you do action rapidly, a lot of important things will be appeared, so that you grasp again on bird's eye.
In order to be these situation worked, it must be always required comfortable environment for employees, so that manager have to create and maintain comfortable environment.
-
No need to add the "meanings" of 3 message, but please place 3 message(Bird's eye view, Agility and Back to comfort) into a poster.
We like some desings below, but you don't need to be swayed too much by them. That is to say, we dont like messy design.
http://www.pixelbazaar.net/design/58203
http://www.pixelbazaar.net/design/49721
http://www.pixelbazaar.net/design/36094
http://www.pixelbazaar.net/design/2736519/poster-design-by-tovel
http://www.pixelbazaar.net/design/2736521/poster-design-by-tovel
http://www.pixelbazaar.net/design/2648092/poster-design-by-lumafoxxen
-
the attachment file is the logo data of our company. Please place it anywhere in the poster.

```html
<!DOCTYPE html>
<html lang="en">
<head>
<meta charset="utf-8">
<title>Principles for Action</title>
<link rel="stylesheet" href="https://fonts.googleapis.com/css2?family=Cinzel:wght@400;500&family=Arimo:wght@400;700&display=swap">
<style>
  :root {
    --sky-top: #bfe0f6;
    --sky-mid: #dcedf9;
    --paper: #ffffff;
    --title-ink: #3a3a3a;
    --heading-blue: #1f7fc1;
    --body-ink: #4a4a4a;
    --rule-blue: #9fcbea;
    --brand-blue: #1b5f98;
  }
  html, body {
    margin: 0;
    padding: 0;
    overflow: hidden;
    background: var(--paper);
  }
  .poster {
    position: relative;
    width: 1200px;
    height: 848px;
    overflow: hidden;
    background: var(--paper);
  }
  .sky {
    position: absolute;
    left: 0;
    top: 0;
    width: 1200px;
    height: 340px;
  }
  .poster-title {
    position: absolute;
    left: 0;
    top: 318px;
    width: 1200px;
    margin: 0;
    text-align: center;
    font-family: "Cinzel", serif;
    font-weight: 400;
    font-size: 70px;
    letter-spacing: 1px;
    color: var(--title-ink);
    line-height: 1;
  }
  .poster-title .initial { font-size: 84px; }
  .principle {
    position: absolute;
    top: 446px;
  }
  .principle-heading {
    margin: 0 0 10px 0;
    font-family: "Cinzel", serif;
    font-weight: 500;
    font-size: 24px;
    color: var(--heading-blue);
    white-space: nowrap;
    line-height: 1.2;
  }
  .principle-heading .initial { font-size: 30px; }
  .principle-text {
    margin: 0;
    font-family: "Arimo", Arial, sans-serif;
    font-size: 14px;
    line-height: 1.32;
    color: var(--body-ink);
  }
  .principle--birds-eye { left: 14px; width: 380px; }
  .principle--birds-eye .principle-text { margin-left: 40px; width: 330px; }
  .principle--agility { left: 420px; width: 350px; }
  .principle--agility .principle-text { margin-left: 46px; width: 300px; }
  .principle--comfort { left: 790px; width: 400px; }
  .principle--comfort .principle-text { margin-left: 40px; width: 345px; }
  .divider {
    position: absolute;
    top: 446px;
    width: 1px;
    height: 192px;
    background: var(--rule-blue);
  }
  .divider--first { left: 406px; }
  .divider--second { left: 778px; }
  .baseline-rule {
    position: absolute;
    left: 59px;
    top: 648px;
    width: 1082px;
    height: 1px;
    background: var(--rule-blue);
  }
  .brand {
    position: absolute;
    left: 0;
    top: 718px;
    width: 1200px;
    display: flex;
    justify-content: center;
    align-items: center;
    gap: 14px;
  }
  .brand-dot {
    width: 22px;
    height: 22px;
    border-radius: 50%;
    background: var(--brand-blue);
  }
  .brand-name {
    font-family: "Arimo", Arial, sans-serif;
    font-weight: 700;
    font-size: 62px;
    letter-spacing: -1px;
    color: var(--brand-blue);
    line-height: 1;
  }
</style>
</head>
<body>
  <main class="poster">
    <svg class="sky" viewBox="0 0 1200 340" role="img" aria-label="Soft blue sky with white clouds drifting across the top of the poster">
      <defs>
        <linearGradient id="skyFade" x1="0" y1="0" x2="0" y2="1">
          <stop offset="0" stop-color="#bfe0f6"/>
          <stop offset="0.55" stop-color="#dcedf9"/>
          <stop offset="1" stop-color="#ffffff"/>
        </linearGradient>
      </defs>
      <rect x="0" y="0" width="1200" height="340" fill="url(#skyFade)"/>
    </svg>

    <h1 class="poster-title"><span class="initial">P</span>RINCIPLES FOR <span class="initial">A</span>CTION</h1>

    <section class="principle principle--birds-eye">
      <h2 class="principle-heading">(1) <span class="initial">B</span>IRD'S EYE VIEW:</h2>
      <p class="principle-text">Although there are multiple right answers, it is difficult to gain something if you do not have different view from common one. We request you always to compare subjective view and objective view and then aim to have the specific view.</p>
    </section>

    <div class="divider divider--first"></div>

    <section class="principle principle--agility">
      <h2 class="principle-heading">(2) <span class="initial">A</span>GILITY:</h2>
      <p class="principle-text">Maximum rapidity is obtained in any case. Rapid accumulation of trivial reply, delivery, and courtesy, and it will lead to overall competitiveness.</p>
    </section>

    <div class="divider divider--second"></div>

    <section class="principle principle--comfort">
      <h2 class="principle-heading">(3) <span class="initial">B</span>ACK <span class="initial">T</span>O <span class="initial">C</span>OMFORT:</h2>
      <p class="principle-text">Whatever the type of business be, various ideas are generated by employees. Those born in uncomfortable environment, become bad product that are not comfortable. In other words, managers will be asked to keep the comfortable environment.</p>
    </section>

    <div class="baseline-rule"></div>

    <footer class="brand">
      <span class="brand-dot"></span>
      <span class="brand-name">nuvelink</span>
    </footer>
  </main>
</body>
</html>
```